Webdesign für Juwelier-Geschäft
Zielgruppe
Wir sind ein Juwelier Laden. Unsere Zielgruppe sind Frauen und Männer jeden Alters, die an Gold- und Silberschmuck/Uhren/Diamanten/Trauringen interessiert sind.
Aufgabenstellung
Edles Design in Gold, Schwarz/Grau, Weiß.
Bildelemente für die Artikelkategorien Ketten, Ohrringe und Ringe etc.
Ein Logo besteht bereits.

```html
<!DOCTYPE html>
<html lang="de">
<head>
<meta charset="utf-8">
<title>Juwelier Orion – Start</title>
<link rel="stylesheet" href="https://fonts.googleapis.com/css2?family=Cormorant+Garamond:wght@500;600&family=Inter:wght@400;500;600&display=swap">
<style>
  :root {
    --gold: #d69a36;
    --gold-soft: #edd4a6;
    --gold-pale: #fdf0dc;
    --cream: #fff6e6;
    --ink: #1b1d3a;
    --grey: #7a7c8c;
    --line: #ececf0;
    --white: #ffffff;
  }
  * { box-sizing: border-box; margin: 0; padding: 0; }
  html, body { width: 866px; height: 1200px; overflow: hidden; background: var(--white); }
  body { position: relative; font-family: "Inter", sans-serif; color: var(--ink); }
  .abs { position: absolute; }

  .nav {
    left: 98px; top: 13px; width: 667px; height: 57px;
    background: var(--white); border-radius: 4px;
    box-shadow: 0 6px 18px rgba(27, 29, 58, 0.08);
  }
  .brand { left: 30px; top: 19px; font-family: "Cormorant Garamond", serif; font-weight: 600; font-size: 14px; letter-spacing: 0.3px; color: var(--ink); display: flex; align-items: center; gap: 5px; white-space: nowrap; }
  .brand-mark { width: 7px; height: 7px; border-radius: 50%; background: var(--gold); }
  .nav-item { top: 29px; font-size: 9px; color: #5b5e78; white-space: nowrap; }
  .nav-item.active { font-weight: 600; color: var(--ink); }
  .nav-item.active::after { content: ""; position: absolute; left: 50%; top: 16px; width: 3px; height: 3px; margin-left: -1.5px; border-radius: 50%; background: var(--gold); }
  .chev { font-size: 7px; margin-left: 2px; }
  .icon { top: 26px; }

  .favourites { left: 61px; top: 98px; width: 753px; height: 349px; background: var(--cream); border-radius: 18px; }

  .section-title { left: 0; width: 866px; text-align: center; font-family: "Cormorant Garamond", serif; font-weight: 500; font-size: 30px; letter-spacing: -0.5px; color: var(--ink); }
  .section-title em { font-style: normal; color: var(--gold); }

  .card { width: 129px; text-align: center; }
  .card-photo { width: 129px; height: 170px; border: 1px solid #cfcfd4; }
  .photo-necklace { background: linear-gradient(180deg, #dcdde2 0%, #f2f2f4 45%, #d8d6d2 100%); }
  .photo-ring { background: linear-gradient(180deg, #8a8a90 0%, #c9c9cc 45%, #f4f4f2 80%, #eef3d8 100%); }
  .card-name { margin-top: 12px; font-family: "Cormorant Garamond", serif; font-size: 11.5px; color: var(--ink); }
  .card-text { margin-top: 5px; font-family: "Cormorant Garamond", serif; font-size: 6.5px; line-height: 12px; color: var(--grey); white-space: nowrap; }
  .card-price { margin-top: 3px; font-family: "Cormorant Garamond", serif; font-size: 9px; color: var(--ink); }
  .card-price span { color: var(--gold); font-weight: 600; }
  .card-button { display: block; margin: 16px auto 0; width: 95px; height: 15px; border-radius: 8px; background: var(--gold-pale); color: var(--gold); font-size: 6px; font-weight: 600; line-height: 15px; letter-spacing: 0.4px; }

  .dot { border-radius: 50%; }

  .contact-tag { left: 116px; top: 937px; width: 196px; height: 19px; border-radius: 10px; background: var(--gold-pale); color: var(--gold); font-size: 7.5px; font-weight: 600; letter-spacing: 2px; line-height: 19px; text-align: center; }
  .contact-mail { left: 116px; top: 980px; font-family: "Cormorant Garamond", serif; font-weight: 500; font-size: 25px; letter-spacing: -0.5px; color: var(--ink); }
  .contact-arrow { left: 365px; top: 979px; width: 30px; height: 30px; border-radius: 50%; background: var(--gold-soft); }
  .social-label { left: 116px; top: 1044px; font-size: 8.5px; color: #5b5e78; }
  .social-button { top: 1035px; width: 29px; height: 29px; border-radius: 50%; border: 1px solid var(--line); display: flex; align-items: center; justify-content: center; }
  .social-button i { width: 7px; height: 7px; border-radius: 50%; background: var(--ink); }

  .links-title { left: 460px; top: 942px; font-size: 8.5px; font-weight: 600; letter-spacing: 1.8px; color: #8a8c9a; }
  .link { font-size: 10.5px; color: var(--ink); }
  .link.strong { font-weight: 600; }

  .divider { left: 116px; top: 1110px; width: 630px; height: 1px; background: var(--line); }
  .copyright { left: 0; top: 1130px; width: 866px; text-align: center; font-size: 8.5px; color: #5b5e78; }
</style>
</head>
<body>

  <header class="nav abs">
    <div class="brand abs">Juwelier Orion <span class="brand-mark"></span></div>
    <span class="nav-item active abs" style="left:139px">Start</span>
    <span class="nav-item abs" style="left:196px">Trauringe <span class="chev">⌄</span></span>
    <span class="nav-item abs" style="left:262px">Reparaturen <span class="chev">⌄</span></span>
    <span class="nav-item abs" style="left:353px">Über uns</span>
    <span class="nav-item abs" style="left:411px">Shop</span>
    <svg class="icon abs" style="left:565px" width="14" height="13" viewBox="0 0 24 22" fill="none" stroke="#1b1d3a" stroke-width="2"><path d="M12 20 3 11a5 5 0 0 1 9-6 5 5 0 0 1 9 6z"/></svg>
    <svg class="icon abs" style="left:588px" width="13" height="13" viewBox="0 0 24 24" fill="none" stroke="#1b1d3a" stroke-width="2.4"><circle cx="10" cy="10" r="7"/><path d="m15 15 7 7"/></svg>
    <svg class="icon abs" style="left:609px" width="15" height="13" viewBox="0 0 26 22" fill="none" stroke="#1b1d3a" stroke-width="2"><path d="M1 2h4l3 13h12l3-9H7"/><circle cx="10" cy="19" r="1.5"/><circle cx="19" cy="19" r="1.5"/></svg>
    <span class="abs dot" style="left:620px;top:24px;width:7px;height:7px;background:var(--gold)"></span>
  </header>

  <span class="dot abs" style="left:47px;top:125px;width:8px;height:8px;background:var(--gold)"></span>

  <section class="favourites abs"></section>
  <h2 class="section-title abs" style="top:112px">Unsere <em>Lieblingstücke</em></h2>

  <div class="card abs" style="left:116px;top:166px">
    <div class="card-photo photo-necklace" role="img" aria-label="Goldene Halskette auf weißer Schmuckbüste"></div>
    <p class="card-name">Halskette</p>
    <p class="card-text">Startups typically begin by a founder (solo-<br>founder) or co-founders who have a way to</p>
    <p class="card-price">Preis: <span>78,99</span></p>
    <span class="card-button">In den Einkaufswagen</span>
  </div>
  <div class="card abs" style="left:280px;top:166px">
    <div class="card-photo photo-necklace" role="img" aria-label="Goldene Halskette auf weißer Schmuckbüste"></div>
    <p class="card-name">Halskette</p>
    <p class="card-text">Startups typically begin by a founder (solo-<br>founder) or co-founders who have a way to</p>
    <p class="card-price">Preis: <span>78,99</span></p>
    <span class="card-button">In den Einkaufswagen</span>
  </div>
  <div class="card abs" style="left:444px;top:166px">
    <div class="card-photo photo-necklace" role="img" aria-label="Goldene Halskette auf weißer Schmuckbüste"></div>
    <p class="card-name">Halskette</p>
    <p class="card-text">Startups typically begin by a founder (solo-<br>founder) or co-founders who have a way to</p>
    <p class="card-price">Preis: <span>78,99</span></p>
    <span class="card-button">In den Einkaufswagen</span>
  </div>
  <div class="card abs" style="left:607px;top:166px">
    <div class="card-photo photo-necklace" role="img" aria-label="Goldene Halskette auf weißer Schmuckbüste"></div>
    <p class="card-name">Halskette</p>
    <p class="card-text">Startups typically begin by a founder (solo-<br>founder) or co-founders who have a way to</p>
    <p class="card-price">Preis: <span>78,99</span></p>
    <span class="card-button">In den Einkaufswagen</span>
  </div>

  <span class="dot abs" style="left:92px;top:429px;width:18px;height:18px;background:var(--gold-soft)"></span>
  <span class="dot abs" style="left:732px;top:461px;width:31px;height:31px;background:var(--gold-soft)"></span>

  <h2 class="section-title abs" style="top:494px">Für <em>Verliebte</em></h2>

  <span class="dot abs" style="left:86px;top:625px;width:11px;height:11px;background:var(--gold-soft)"></span>

  <div class="card abs" style="left:116px;top:547px">
    <div class="card-photo photo-ring" role="img" aria-label="Foto: Verlobungsring auf Ringhalter"></div>
    <p class="card-name">Verlobungsring</p>
    <p class="card-text">Startups typically begin by a founder (solo-<br>founder) or co-founders who have a way to</p>
    <p class="card-price">Preis: <span>78,99</span></p>
    <span class="card-button">In den Einkaufswagen</span>
  </div>
  <div class="card abs" style="left:280px;top:547px">
    <div class="card-photo photo-ring" role="img" aria-label="Foto: Verlobungsring auf Ringhalter"></div>
    <p class="card-name">Verlobungsring</p>
    <p class="card-text">Startups typically begin by a founder (solo-<br>founder) or co-founders who have a way to</p>
    <p class="card-price">Preis: <span>78,99</span></p>
    <span class="card-button">In den Einkaufswagen</span>
  </div>
  <div class="card abs" style="left:444px;top:547px">
    <div class="card-photo photo-ring" role="img" aria-label="Foto: goldener Trauring auf Ringhalter"></div>
    <p class="card-name">Trauring</p>
    <p class="card-text">Startups typically begin by a founder (solo-<br>founder) or co-founders who have a way to</p>
    <p class="card-price">Preis: <span>78,99</span></p>
    <span class="card-button">In den Einkaufswagen</span>
  </div>
  <div class="card abs" style="left:607px;top:547px">
    <div class="card-photo photo-ring" role="img" aria-label="Foto: goldener Trauring auf Ringhalter"></div>
    <p class="card-name">Trauring</p>
    <p class="card-text">Startups typically begin by a founder (solo-<br>founder) or co-founders who have a way to</p>
    <p class="card-price">Preis: <span>78,99</span></p>
    <span class="card-button">In den Einkaufswagen</span>
  </div>

  <span class="dot abs" style="left:52px;top:785px;width:20px;height:20px;background:var(--gold-pale)"></span>
  <span class="dot abs" style="left:663px;top:848px;width:34px;height:34px;background:var(--gold)"></span>

  <footer>
    <div class="contact-tag abs">WAS KÖNNEN WIR FÜR SIE TUN?</div>
    <p class="contact-mail abs">Hello@juwelierorion.de</p>
    <div class="contact-arrow abs">
      <svg width="30" height="30" viewBox="0 0 30 30" fill="none" stroke="#ffffff" stroke-width="1.3"><path d="M12 18l6-6M13 12h5v5"/></svg>
    </div>
    <p class="social-label abs">Social Media</p>
    <span class="social-button abs" style="left:181px" aria-label="Social Media 1"><i></i></span>
    <span class="social-button abs" style="left:218px" aria-label="Social Media 2"><i></i></span>
    <span class="social-button abs" style="left:255px" aria-label="Social Media 3"><i></i></span>

    <p class="links-title abs">QUICK LINKS</p>
    <a class="link strong abs" style="left:460px;top:976px">Home</a>
    <a class="link abs" style="left:460px;top:1000px">Journey</a>
    <a class="link abs" style="left:460px;top:1024px">Technology</a>
    <a class="link abs" style="left:460px;top:1048px">Team</a>
    <a class="link abs" style="left:568px;top:976px">Vision</a>
    <a class="link abs" style="left:568px;top:1000px">Thinking</a>
    <a class="link abs" style="left:568px;top:1024px">Join us</a>
    <a class="link abs" style="left:568px;top:1048px">Connect</a>
    <a class="link abs" style="left:663px;top:976px">Privacy &amp; Terms</a>
    <a class="link abs" style="left:663px;top:1000px">Glenmoor</a>
    <a class="link abs" style="left:663px;top:1024px">Alderfield</a>

    <div class="divider abs"></div>
    <p class="copyright abs">Copyright 2022. All rights reserved.</p>
  </footer>

</body>
</html>
```